**Promotional Flyer for Charity Golf Event**

Create a promotional flyer for a Charity Golf Event

Target Market(s)

Golfers wanting to play in a charity/corporate golf event

Industry/Entity Type

Non Profit

Requirements
Must have
• The flyer must have the logo of the charity (Bluefinch), must have the logo of the Golf Event (Tarn Invitational) and the Velmora Logo and the text supplied.
• Photo supplied to also be included

```html
<!DOCTYPE html>
<html lang="en">
<head>
<meta charset="utf-8">
<title>The Velmora Tarn Invitational 2017 – Flyer</title>
<link href="https://fonts.googleapis.com/css2?family=Lato:wght@400;700;900&family=Questrial&family=Noto+Serif:ital,wght@1,700&display=swap" rel="stylesheet">
<style>
  :root{
    --green:#1b6b3a;
    --green-dark:#145530;
    --ink:#1d1d1d;
    --text:#333;
    --orange:#f05a28;
    --gold:#f2b233;
    --page:#ffffff;
    --backdrop:#d6d6d6;
  }
  *{box-sizing:border-box;margin:0;padding:0}
  html,body{width:1200px;height:1047px;overflow:hidden}
  body{background:var(--backdrop);position:relative;font-family:'Lato',sans-serif;color:var(--text)}
  .page{position:absolute;top:126px;width:567px;height:794px;background:var(--page);overflow:hidden}
  .front{left:22px}
  .back{left:614px}
  .abs{position:absolute}

  /* Front */
  .front-photo{position:absolute;left:0;top:170px;width:100%;height:624px;
    background:linear-gradient(180deg,#ffffff 0%,#f7ead0 12%,#f0c873 32%,#c9902e 46%,#7d7a36 58%,#3f4a24 70%,#1f1f1b 82%,#1b1b1b 100%)}
  .title-the{left:104px;top:20px;font-family:'Questrial',sans-serif;font-size:58px;color:var(--ink);line-height:1}
  .title-main{left:104px;top:72px;font-family:'Lato',sans-serif;font-weight:900;font-size:55px;color:var(--green);line-height:1;letter-spacing:1px}
  .title-sub{right:66px;top:120px;font-family:'Noto Serif',serif;font-style:italic;font-weight:700;font-size:38px;color:var(--green);line-height:1}
  .date-block{left:152px;top:594px;width:264px;height:46px;border-left:5px double #fff;border-right:5px double #fff;text-align:center;color:#fff}
  .date-line{font-family:'Lato',sans-serif;font-weight:700;font-size:20px;line-height:22px}
  .day-line{font-weight:700;font-size:20px;letter-spacing:14px;line-height:24px;padding-left:14px}
  .center-text{left:0;width:100%;text-align:center;color:#fff}
  .venue{top:651px;font-weight:700;font-size:13px;line-height:16px}
  .memorial{top:694px;font-family:'Questrial',sans-serif;font-size:12px;line-height:15px}
  .memorial b{font-family:'Lato',sans-serif;font-size:13px}
  .quote{top:732px;left:100px;width:400px;font-family:'Questrial',sans-serif;font-size:11px;line-height:13px;color:#fff;text-align:center}
  .event-name{left:26px;top:744px;color:#fff;font-family:'Questrial',sans-serif;font-size:15px;line-height:16px}
  .velmora-mark{display:flex;align-items:center;gap:5px;font-family:'Questrial',sans-serif;font-size:14px}
  .velmora-mark .sq{width:14px;height:14px;background:var(--gold)}
  .front .velmora-mark{right:26px;top:746px;color:#fff}

  /* Back */
  .back-photo{position:absolute;left:0;top:0;width:100%;height:386px;
    background:linear-gradient(180deg,#7fb24a 0%,#9cc46a 35%,#d8e3c8 70%,#f6f6f6 100%)}
  .ribbon{left:23px;top:386px;width:520px;height:46px}
  .ribbon-text{left:23px;top:393px;width:520px;text-align:center;color:#fff;font-size:11px;line-height:15px}
  .pill{display:inline-block;background:var(--green);color:#fff;font-weight:700;font-size:10px;letter-spacing:.6px;padding:2px 7px;border-radius:7px;line-height:12px}
  .list{list-style:none;font-size:11px;line-height:16.5px;color:var(--text)}
  .list li{position:relative;padding-left:10px}
  .list li::before{content:"";position:absolute;left:0;top:4px;border-left:5px solid var(--green);border-top:4px solid transparent;border-bottom:4px solid transparent}
  .body-copy{font-size:11px;line-height:14px;color:var(--text)}
  .email{display:flex;align-items:center;gap:7px;font-weight:700;font-size:11px;color:var(--ink)}
  .price-box{left:317px;top:570px;width:202px;height:121px;border:2px solid var(--green);border-radius:10px;text-align:center}
  .price-kicker{margin-top:9px;font-weight:700;font-size:9px;line-height:10px;color:var(--ink)}
  .price-heading{font-weight:900;font-size:15px;line-height:16px;letter-spacing:.5px;color:var(--ink)}
  .price-type{font-family:'Questrial',sans-serif;font-size:13px;margin-top:5px;color:var(--ink)}
  .price-big{font-weight:900;font-size:21px;color:var(--green);line-height:24px;margin-top:3px}
  .price-incl{font-size:6.5px;color:var(--ink);margin-top:2px}
  .price-dinner{font-weight:700;font-size:8px;color:var(--ink)}
  .price-dinner span{font-weight:900;font-size:16px;color:var(--green)}
  .footer{left:0;top:716px;width:100%;height:78px;border-top:1px solid #777;background:linear-gradient(180deg,#f7f7f7,#e6e6e6)}
  .footer .event-name{left:23px;top:24px;color:#666}
  .tickets{left:152px;top:30px;display:flex;align-items:center;gap:5px;font-size:9px;color:var(--ink)}
  .tickets b{font-size:22px;font-weight:900;color:var(--orange);letter-spacing:.3px}
  .footer .velmora-mark{right:22px;top:28px;color:#555}
</style>
</head>
<body>

<section class="page front">
  <div class="front-photo" role="img" aria-label="Golfer finishing a swing on a fairway at sunset, hills and trees behind"></div>
  <div class="abs title-the">The</div>
  <div class="abs title-main">VELMORA TARN</div>
  <div class="abs title-sub">Invitational 2017</div>

  <div class="abs date-block">
    <div class="date-line">22nd September 2017</div>
    <div class="day-line">FRIDAY</div>
  </div>
  <p class="abs center-text venue">Harlow Ridge Golf Club, 14 Ferris Road,<br>Eastbrook Harlow</p>
  <p class="abs center-text memorial">Inaugural VELMORA Tarn Invitational 2017 in memory of<br><b>Liam Ardent and for Bluefinch</b></p>
  <p class="abs quote">“ Come along and join us in supporting Bluefinch as they provide essential services to children young people and their families with cancer ”</p>
  <div class="abs event-name">Tarn<br>Invitational</div>
  <div class="abs velmora-mark"><span class="sq"></span>Velmora</div>
</section>

<section class="page back">
  <div class="back-photo" role="img" aria-label="Smiling golfer waving from a golf cart on the course"></div>

  <svg class="abs ribbon" viewBox="0 0 520 46" aria-hidden="true">
    <polygon points="0,23 26,0 520,0 497,23 520,46 26,46" fill="var(--green)"/>
  </svg>
  <p class="abs ribbon-text">Not a golfer but keen to support the Inaugural<br><b>VELMORA Tarn Invitational and Bluefinch</b> then why not join us and be inspired</p>

  <div class="abs" style="left:23px;top:462px">
    <span class="pill">PLAY FORMAT :</span>
    <ul class="list" style="margin-top:8px"><li>4 ball ambrose, shotgun start.</li></ul>
  </div>

  <div class="abs" style="left:23px;top:519px">
    <span class="pill">GREAT EVENT PRIZES</span>
    <ul class="list" style="margin-top:10px">
      <li>Perpetual Tarn Invitational Trophy</li>
      <li>Longest Drive Trophy</li>
      <li>Nearest to the Pin</li>
    </ul>
  </div>

  <div class="abs" style="left:238px;top:462px">
    <span class="pill">FORMAT :</span>
    <ul class="list" style="margin-top:8px">
      <li>1 pm Registration and light lunch at Harlow Ridge Golf Club</li>
      <li>2 pm Shotgun start, play commences</li>
      <li>5 pm Gourmet BBQ and drinks – presentation and prizes</li>
      <li>7.30 pm Finish</li>
    </ul>
  </div>

  <div class="abs" style="left:23px;top:614px;width:270px">
    <span class="pill">SPONSORSHIP OPPORTUNITIES</span>
    <p class="body-copy" style="margin-top:8px">We have opportunities for Hole Sponsors, as well as a Drink Cart Sponsor that start from $1,300 please email :</p>
    <div class="email" style="margin-top:8px">
      <svg width="14" height="10" viewBox="0 0 14 10" aria-hidden="true"><rect x=".5" y=".5" width="13" height="9" fill="none" stroke="var(--green)"/><path d="M.5 .5 7 6 13.5 .5M.5 9.5 5 5M13.5 9.5 9 5" fill="none" stroke="var(--green)"/></svg>
      clara.wynn@velmoragroup.com
    </div>
  </div>

  <div class="abs price-box">
    <div class="price-kicker">PLAYER AND SPONSORSHIP</div>
    <div class="price-heading">OPPORTUNITIES</div>
    <div class="price-type">Golf-Individual Player</div>
    <div class="price-big">$187.50</div>
    <div class="price-incl">▸ Light lunch ▸ 9 Holes of Golf ▸ Gourmet</div>
    <div class="price-dinner">Dinner Only <span>$75</span></div>
  </div>

  <footer class="abs footer">
    <div class="abs event-name">Tarn<br>Invitational</div>
    <div class="abs tickets">Tickets can be purchased through: <b>Ticketloom</b></div>
    <div class="abs velmora-mark"><span class="sq"></span>Velmora</div>
  </footer>
</section>

</body>
</html>
```